Conservative, Modern and Sharp Builder Business card

Hi there,
We would like to update our existing business card.
I have attached photos of existing business card, logo and van sign.

I would like the business card to also list what we do :
Renovation • New Build • Alteration
Extension • Bathroom • Maintenance.(Seperated by dots)

Contact number : 021 0483 0752
(With that exact spacing)

Ideally when people looking from about 2-3 metres, they know that it is a builder’s business card

Open to suggestions on fonts, layout, style of business card

PLEASE ONLY SUBMIT YOUR BEST OR MAX 3 DESIGNS FOR EACH DESIGNER

Thanks

Industry/Entity Type

Construction. Renovation

Contact Information for Business Card

Details should be the same as the existing card. And addition of what we do.

Requirements
Should not have
• The new business card must not have the same layout as our existing one. Thanks

```html
<!DOCTYPE html>
<html lang="en">
<head>
<meta charset="utf-8">
<title>KeelCraft Business Card</title>
<link href="https://fonts.googleapis.com/css2?family=Montserrat:wght@400;600;700&family=Oswald:wght@600&family=Poppins:wght@700&display=swap" rel="stylesheet">
<style>
  :root{
    --backdrop:#3a3a3a;
    --ink:#111111;
    --paper:#ffffff;
    --muted:#6b6b6b;
    --card-black:#0d0d0d;
  }
  *{box-sizing:border-box;margin:0;padding:0}
  html,body{width:1200px;height:1200px;overflow:hidden}
  body{background:var(--backdrop);position:relative;font-family:"Montserrat",sans-serif}
  .card{position:absolute;left:162px;width:876px;height:500px;border-radius:34px;overflow:hidden;box-shadow:0 14px 30px rgba(0,0,0,.45)}
  .card--front{top:70px;background:var(--paper);color:var(--ink)}
  .card--back{top:630px;background:var(--card-black);color:var(--paper);display:flex;align-items:center;justify-content:center}

  .brand{display:flex;align-items:center;gap:16px;font-family:"Poppins",sans-serif;font-weight:700;letter-spacing:-1px}
  .brand__mark{display:block;background:currentColor}
  .card--front .brand{position:absolute;right:70px;top:130px;font-size:66px}
  .card--front .brand__mark{width:22px;height:22px}
  .card--back .brand{font-size:104px}
  .card--back .brand__mark{width:34px;height:34px}

  .holder{position:absolute;left:56px;top:150px}
  .holder__name{font-weight:700;font-size:34px;letter-spacing:1px;line-height:1}
  .holder__role{font-weight:400;font-size:18px;letter-spacing:1.5px;color:var(--muted);margin-top:4px}
  .contacts{list-style:none;margin-top:22px}
  .contacts li{display:flex;align-items:center;gap:12px;font-size:21px;line-height:1;margin-bottom:12px}
  .contacts svg{width:22px;height:22px;flex:none}
  .icon-square{width:18px;height:18px;border:2.5px solid var(--ink);border-radius:4px;flex:none;margin:0 2px}

  .services{position:absolute;left:0;right:0;bottom:56px;height:44px;background:var(--ink);color:var(--paper);
    font-family:"Oswald",sans-serif;font-weight:600;font-size:21px;letter-spacing:1px;text-transform:uppercase;
    display:flex;align-items:center;justify-content:center;gap:12px}
  .services .dot{font-size:16px}
</style>
</head>
<body>
  <section class="card card--front">
    <div class="holder">
      <p class="holder__name">DANIEL MOREAU</p>
      <p class="holder__role">RESIDENTIAL BUILDER</p>
      <ul class="contacts">
        <li><svg viewBox="0 0 24 24"><path fill="#111" d="M6.6 10.8a15 15 0 0 0 6.6 6.6l2.2-2.2c.3-.3.7-.4 1-.2 1.1.4 2.3.6 3.6.6.6 0 1 .4 1 1V20c0 .6-.4 1-1 1A17 17 0 0 1 3 4c0-.6.4-1 1-1h3.5c.6 0 1 .4 1 1 0 1.3.2 2.5.6 3.6.1.3 0 .7-.2 1z"/></svg>021 0483 0752</li>
        <li><svg viewBox="0 0 24 24"><rect x="2" y="5" width="20" height="14" fill="none" stroke="#111" stroke-width="2"/><path d="M2 5l10 8 10-8" fill="none" stroke="#111" stroke-width="2"/></svg>hello@keelcraft.co.nz</li>
        <li><svg viewBox="0 0 24 24" fill="none" stroke="#111" stroke-width="1.8"><circle cx="12" cy="12" r="9.5"/><ellipse cx="12" cy="12" rx="4" ry="9.5"/><path d="M2.5 12h19M4 7h16M4 17h16"/></svg>www.KeelCraft.nz</li>
        <li><span class="icon-square"></span>@KeelCraft</li>
      </ul>
    </div>
    <div class="brand"><span class="brand__mark"></span>KeelCraft</div>
    <div class="services">
      <span>Renovation</span><span class="dot">●</span><span>New Build</span><span class="dot">●</span><span>Alteration</span><span class="dot">●</span><span>Extension</span><span class="dot">●</span><span>Bathroom</span><span class="dot">●</span><span>Maintenance</span>
    </div>
  </section>

  <section class="card card--back">
    <div class="brand"><span class="brand__mark"></span>KeelCraft</div>
  </section>
</body>
</html>
```